Spanish Student Needs a Cover for his PhD Dissertation

Hi everyone :) So, I'm a Corneal surgeon currently finishing my PhD, with a dissertation focused on the evaluation of quality of life in patients affected by a disease called Keratoconus. Just so you know, Keratoconus is a condition in which the cornea (the frontal part of the way) gets thin and bulgy and it decreases vision. What I did during my PhD was designing a questionnaire for evaluating quality of life in this kind of patients.
I need to design a hard cover for my dissertation, which is 200 sheets long. I like kind of minimalistic and geometric designs but I am totally open to suggestions. What needs to be in the cover is the name of the dissertation "Diseño, desarrollo y validación de una encuesta para evaluar el compromiso visual y emocional subjetivos en pacientes con Queratocono" and my name, "Iñigo Tarrasco". The other thing that needs to go there is the logo of my university (Universidad de Montebrisa). Aside from that, anything else is up to the designer. It would be important to use the kind of "red" color I am using in the dissertation. I am attaching the frontal page of my dissertation so you know what kind of design and colors I am using.
In the back part, of the cover, there should be this small inscription: "Iñigo Tarrasco, MD, es un Oftalmólogo Subespecialista en Cirugía Refractiva de la Universidad Serrana Metropolitana (Colombia) y la Universidad de Montebrisa (España). Actualmente se desempeña como miembro del Departamento de Córnea y Cirugía Refractiva de la Clínica de Oftalmología Vallealto y como director de su propia compañía de emprendimiento médico Silver Heron Surgical". Please leave a space to place my picture; I will have it taken this week so I don't have it right now, you can just leave the blank spot and I will include it later
The size of the pages is standard "letter" size.
Thanks a lot!

Target Market(s)

PhD Scholars

Font styles to use
Serif

Requirements
Must have
• The "red" color I use on my font. It must be formal but "young".
Nice to have
• I like to keep the design clean, kind of "formal with a young" touch so to speak. I really like gray colors, so it would be nice to have broad areas of gray. I love geometrical designs.
I have uploaded a very early version a friend of mine made (it even had a different title); this can be a starting point for you to work on, but I am more than open to suggestions and new ideas.
Should not have
• Please don't use my whole name, Iñigo Tarrasco is fine. I don't like ALL CAPITALS.

```html
<!DOCTYPE html>
<html lang="es">
<head>
<meta charset="utf-8">
<title>Cubierta de tesis doctoral – Iñigo Tarrasco</title>
<link rel="stylesheet" href="https://fonts.googleapis.com/css2?family=Barlow:wght@400;500;700&family=Roboto+Condensed:wght@700&display=swap">
<style>
  :root {
    --backdrop: #e4e4e4;
    --charcoal: #333333;
    --charcoal-deep: #2b2b2b;
    --graphite: #4a4a4a;
    --brand-red: #b5172f;
    --brand-red-dark: #8c1224;
    --paper: #ffffff;
    --silver: #d9d9d9;
    --ink: #222222;
    --line-gold: #f2a21b;
    --line-red: #d8232a;
  }
  * { box-sizing: border-box; margin: 0; padding: 0; }
  html, body {
    width: 1200px; height: 1142px; overflow: hidden;
    background: radial-gradient(ellipse at 50% 40%, #f1f1f1 0%, var(--backdrop) 75%);
  }
  .spread { position: relative; width: 1200px; height: 1142px; }
  .cover {
    position: absolute; top: 260px; width: 480px; height: 621px;
    overflow: hidden; background: var(--charcoal);
    box-shadow: 0 18px 40px rgba(0,0,0,.18);
  }
  .cover--front { left: 80px; }
  .cover--back { left: 640px; background: var(--charcoal-deep); }
  .cover-shapes { position: absolute; inset: 0; width: 100%; height: 100%; }

  /* Front cover */
  .institution {
    position: absolute; top: 92px; right: 16px; width: 172px;
    text-align: center; font-family: "Barlow", sans-serif;
  }
  .institution-mark {
    width: 44px; height: 44px; margin: 0 auto 8px;
    border: 2px solid var(--brand-red); border-radius: 50%;
  }
  .institution-name {
    font-weight: 700; font-size: 13.5px; line-height: 1.2;
    color: var(--brand-red); white-space: nowrap;
  }
  .doctoral-school {
    margin-top: 14px; font-weight: 700; font-size: 11px; color: var(--ink);
  }
  .title-block {
    position: absolute; left: 46px; top: 440px; width: 222px;
    font-family: "Roboto Condensed", sans-serif;
  }
  .accent-rule {
    height: 2px; width: 118px;
    background: linear-gradient(90deg, var(--line-gold), var(--line-red));
  }
  .dissertation-title {
    margin: 8px 0 8px; color: var(--paper);
    font-size: 18px; line-height: 1.08; font-weight: 700;
  }
  .author {
    margin-top: 8px; font-family: "Barlow", sans-serif; font-weight: 400;
    font-size: 15px; color: #cfcfcf; letter-spacing: .6px;
  }

  /* Back cover */
  .portrait-slot {
    position: absolute; left: 102px; top: 80px; width: 74px; height: 86px;
    background: linear-gradient(180deg, #dcdcdc, #bdbdbd);
  }
  .author-bio {
    position: absolute; left: 104px; top: 178px; width: 240px;
    font-family: "Barlow", sans-serif; font-size: 12px; line-height: 1.4;
    color: #e6e6e6; font-weight: 400;
  }
  .author-bio strong {
    display: block; font-weight: 700; font-size: 13.5px; color: var(--paper);
  }
</style>
</head>
<body>
<main class="spread">

  <section class="cover cover--front" aria-label="Portada">
    <svg class="cover-shapes" viewBox="0 0 480 621" preserveAspectRatio="none">
      <defs>
        <linearGradient id="photoTone" x1="0" y1="0" x2="1" y2="1">
          <stop offset="0" stop-color="#9a9a9a"/>
          <stop offset=".5" stop-color="#6e6e6e"/>
          <stop offset="1" stop-color="#3d3d3d"/>
        </linearGradient>
        <linearGradient id="redTone" x1="0" y1="0" x2="1" y2="1">
          <stop offset="0" stop-color="#a3142a"/>
          <stop offset=".6" stop-color="#c01b33"/>
          <stop offset="1" stop-color="#b5172f"/>
        </linearGradient>
      </defs>
      <polygon points="0,0 480,0 480,40 265,155 0,310" fill="url(#redTone)"/>
      <polygon points="265,155 480,40 480,505" fill="var(--paper)"/>
      <g role="img" aria-label="Fotografía en blanco y negro de un ojo de perfil con la córnea abombada">
        <polygon points="0,310 265,155 480,505 420,565 0,390" fill="url(#photoTone)"/>
      </g>
      <polygon points="480,505 480,621 300,621" fill="var(--graphite)"/>
    </svg>

    <div class="institution">
      <div class="institution-mark"></div>
      <p class="institution-name">Universidad de Montebrisa</p>
      <p class="doctoral-school">Escuela Doctoral Montebrisa</p>
    </div>

    <div class="title-block">
      <div class="accent-rule"></div>
      <h1 class="dissertation-title">Diseño, desarrollo y validación de una encuesta para evaluar el compromiso visual y emocional subjetivos en pacientes con Queratocono</h1>
      <div class="accent-rule"></div>
      <p class="author">Iñigo Tarrasco</p>
    </div>
  </section>

  <section class="cover cover--back" aria-label="Contraportada">
    <svg class="cover-shapes" viewBox="0 0 480 621" preserveAspectRatio="none">
      <defs>
        <linearGradient id="maroonFade" x1="0" y1="0" x2="1" y2="1">
          <stop offset="0" stop-color="#1c1c1c"/>
          <stop offset="1" stop-color="#5a0f1b"/>
        </linearGradient>
        <linearGradient id="silverSheen" x1="0" y1="0" x2="1" y2="1">
          <stop offset="0" stop-color="#f2f2f2"/>
          <stop offset=".6" stop-color="#d6d6d6"/>
          <stop offset="1" stop-color="#bcbcbc"/>
        </linearGradient>
      </defs>
      <polygon points="0,373 240,515 140,621 0,621" fill="url(#maroonFade)"/>
      <polygon points="240,515 140,621 365,621" fill="var(--brand-red)"/>
      <polygon points="240,515 480,310 480,621 365,621" fill="url(#silverSheen)"/>
    </svg>

    <div class="portrait-slot" role="img" aria-label="Espacio reservado para la fotografía del autor"></div>

    <p class="author-bio">
      <strong>Iñigo Tarrasco, MD,</strong>
      es un Oftalmólogo Subespecialista en Cirugía Refractiva de la Universidad Serrana Metropolitana (Colombia) y la Universidad de Montebrisa (España). Actualmente se desempeña como miembro del Departamento de Córnea y Cirugía Refractiva de la Clínica de Oftalmología Vallealto y como director de su propia compañía de emprendimiento médico Silver Heron Surgical
    </p>
  </section>

</main>
</body>
</html>
```